Web page design for podiatry office*

Need a web page for our podiatry office. It should feature most of our services, hours, directions and location. Should include a short bio of the doctor and a contact page.

Coding

Coded - Design and coding required

Number of Pages Required

1 page

Colors

Designer to choose colors to be used in the design.

```html
<!DOCTYPE html>
<html lang="en">
<head>
<meta charset="utf-8">
<title>Podiatry Office</title>
<link href="https://fonts.googleapis.com/css2?family=Montserrat:wght@300;400;500;600;700&display=swap" rel="stylesheet">
<style>
:root{
  --navy:#1c2541;
  --navy-deep:#141b33;
  --hero-a:#2b3a5c;
  --hero-b:#1d2744;
  --blue:#1e88e5;
  --blue-bright:#2196f3;
  --text:#333a45;
  --muted:#7a818c;
  --white:#ffffff;
  --map:#e4e6e9;
  --social-blue:#3b6fd8;
  --social-sky:#3e9be8;
  --social-red:#e53935;
}
*{box-sizing:border-box;margin:0;padding:0}
html,body{width:1200px;height:2268px;overflow:hidden}
body{font-family:'Montserrat',sans-serif;color:var(--text);background:var(--white);position:relative}
section,header,footer{position:absolute;left:0;width:1200px}
.btn{display:inline-block;background:var(--blue);color:var(--white);font-size:13px;font-weight:600;border-radius:20px;padding:10px 26px}

/* hero */
.hero{top:0;height:580px;background:linear-gradient(160deg,var(--hero-a),var(--hero-b))}
.nav{position:absolute;top:18px;left:24px;right:60px;display:flex;justify-content:space-between;align-items:center}
.brand{display:flex;align-items:center;gap:10px;color:var(--white);font-weight:600;font-size:18px}
.brand-mark{width:22px;height:22px;border-radius:50%;background:var(--blue-bright)}
.menu{display:flex;gap:40px;font-size:13px;color:var(--white)}
.menu .active{color:var(--blue-bright)}
.hero-copy{position:absolute;top:205px;width:100%;text-align:center}
.hero-copy h1{font-size:50px;font-weight:700;line-height:60px}
.hero-copy .accent{color:var(--blue-bright)}
.hero-copy .light{color:var(--white)}
.hero-copy p{color:var(--white);font-size:15px;margin:8px 0 30px}

/* services */
.services{top:580px;height:452px;text-align:center}
.services h2{font-size:34px;font-weight:400;margin-top:40px;color:var(--text)}
.service-grid{display:flex;justify-content:center;gap:48px;margin-top:60px;text-align:left}
.service{width:196px}
.service svg{display:block;margin-bottom:20px}
.service h3{font-size:16px;font-weight:500;margin-bottom:12px}
.service p{font-size:11px;line-height:16px;color:var(--muted)}
.services .btn{margin-top:46px;padding:9px 22px;font-size:12px}

/* doctor */
.doctor{top:1032px;height:400px}
.doctor-photo{position:absolute;left:0;top:0;width:600px;height:400px;background:linear-gradient(135deg,#c9d3dc,#8797a6)}
.doctor-bio{position:absolute;left:640px;top:70px;width:440px}
.doctor-bio h2{font-size:48px;font-weight:400;margin-bottom:28px}
.doctor-bio p{font-size:11px;line-height:17px;color:var(--muted);margin-bottom:16px}
.doctor-bio .btn{margin-top:8px;padding:9px 22px;font-size:12px}

/* location */
.location{top:1432px;height:336px}
.map{position:absolute;inset:0;background:var(--map)}
.address-card{position:absolute;left:192px;top:0;width:304px;height:336px;background:var(--blue-bright);color:var(--white);text-align:center;padding-top:78px}
.address-card p{font-size:12px;line-height:18px;margin-top:14px}
.address-card .hours{font-size:11px;line-height:17px;margin-top:10px}
.address-card .btn-light{display:inline-block;margin-top:18px;background:var(--white);color:var(--blue);font-size:11px;font-weight:600;border-radius:16px;padding:7px 18px}

/* contact */
.contact{top:1768px;height:424px;background:linear-gradient(160deg,#2a3658,var(--navy))}
.contact h2{position:absolute;left:200px;top:64px;font-size:46px;font-weight:600;color:var(--white)}
.contact-info{position:absolute;left:200px;top:140px;font-size:16px;line-height:24px;color:var(--white)}
.contact-info span{color:var(--blue-bright)}
.social{position:absolute;left:204px;top:276px;display:flex;gap:20px}
.social i{display:block;width:30px;height:30px;border-radius:50%}
.contact-form{position:absolute;left:600px;top:78px;width:400px}
.field{height:34px;border:1px solid rgba(255,255,255,.35);color:var(--white);font-size:11px;padding:10px 12px;margin-bottom:12px}
.field.message{height:90px}
.contact-form .btn{position:absolute;right:0;top:264px;padding:9px 22px;font-size:12px}

/* footer */
.footer{top:2192px;height:76px;background:var(--navy-deep);color:var(--white);font-size:11px;display:flex;justify-content:space-between;align-items:center;padding:0 200px}
.footer nav{display:flex;gap:22px}
</style>
</head>
<body>

<header class="hero">
  <div class="nav">
    <div class="brand"><span class="brand-mark"></span>Your Logo</div>
    <nav class="menu"><span>Home</span><span class="active">Services</span><span>About us</span><span>Contact Us</span></nav>
  </div>
  <div class="hero-copy">
    <h1 class="accent">Foot or Ankle Pain ?</h1>
    <h1 class="light">We're here for you !</h1>
    <p>Expert foot and ankle care for the whole family.</p>
    <span class="btn">Learn more</span>
  </div>
</header>

<section class="services">
  <h2>Our services</h2>
  <div class="service-grid">
    <div class="service">
      <svg width="40" height="34" viewBox="0 0 40 34" fill="none" stroke="#1e88e5" stroke-width="2"><rect x="2" y="2" width="36" height="30" rx="2"/><line x1="2" y1="10" x2="38" y2="10"/><line x1="8" y1="18" x2="32" y2="18"/><line x1="8" y1="24" x2="24" y2="24"/></svg>
      <h3>Heel pain care</h3>
      <p>Diagnosis and treatment of plantar fasciitis, heel spurs and Achilles pain so you can walk in comfort again.</p>
    </div>
    <div class="service">
      <svg width="40" height="34" viewBox="0 0 40 34" fill="none" stroke="#1e88e5" stroke-width="2"><rect x="10" y="14" width="20" height="18" rx="2"/><path d="M14 14V9a6 6 0 0 1 12 0v5"/><line x1="20" y1="21" x2="20" y2="26"/></svg>
      <h3>Diabetic foot care</h3>
      <p>Regular checks, wound care and nail care that protect feet at risk and help prevent serious problems.</p>
    </div>
    <div class="service">
      <svg width="40" height="34" viewBox="0 0 40 34" fill="none" stroke="#1e88e5" stroke-width="2"><rect x="2" y="2" width="36" height="24" rx="2"/><line x1="14" y1="32" x2="26" y2="32"/><line x1="20" y1="26" x2="20" y2="32"/><polyline points="8,20 15,13 21,17 31,8"/></svg>
      <h3>Sports injuries</h3>
      <p>Care for sprains, fractures and overuse injuries with a clear plan to get you back to your sport.</p>
    </div>
    <div class="service">
      <svg width="40" height="34" viewBox="0 0 40 34" fill="none" stroke="#1e88e5" stroke-width="2"><path d="M20 2a10 10 0 0 0-6 18v4h12v-4a10 10 0 0 0-6-18z"/><line x1="15" y1="28" x2="25" y2="28"/><line x1="17" y1="32" x2="23" y2="32"/></svg>
      <h3>Custom orthotics</h3>
      <p>Made-to-measure insoles from a gait study that ease pain in the feet, knees and lower back.</p>
    </div>
  </div>
  <span class="btn">Find more</span>
</section>

<section class="doctor">
  <div class="doctor-photo" role="img" aria-label="Portrait photo of the doctor in a white coat with a stethoscope"></div>
  <div class="doctor-bio">
    <h2>Jon Doe</h2>
    <p>Dr. Doe is a board-certified podiatrist with more than fifteen years of experience treating foot and ankle conditions in patients of every age.</p>
    <p>He trained in podiatric medicine and surgery and takes a special interest in sports injuries, diabetic foot care and minimally invasive treatment.</p>
    <p>Patients value his calm manner and clear advice. He takes time to explain every option and builds each care plan around daily life.</p>
    <span class="btn">Learn more</span>
  </div>
</section>

<section class="location">
  <div class="map" role="img" aria-label="Street map showing the office location"></div>
  <div class="address-card">
    <svg width="20" height="28" viewBox="0 0 20 28"><path d="M10 0a10 10 0 0 0-10 10c0 7 10 18 10 18s10-11 10-18A10 10 0 0 0 10 0z" fill="#fff"/><circle cx="10" cy="10" r="4" fill="#2196f3"/></svg>
    <p>214 Elm Avenue<br>Springfield, UK</p>
    <p class="hours">Mon – Fri: 8:00 – 18:00<br>Sat: 9:00 – 13:00 · Sun: closed</p>
    <span class="btn-light">Get Directions</span>
  </div>
</section>

<section class="contact">
  <h2>Contact with us</h2>
  <div class="contact-info">
    <div>Address : <span>48 Harbor Lane, Springfield</span></div>
    <div>Phone : <span>+1 555 0142 880</span></div>
    <div>E-mail : <span>hello@steppodiatry.com</span></div>
  </div>
  <div class="social">
    <i style="background:var(--social-blue)"></i>
    <i style="background:var(--social-sky)"></i>
    <i style="background:var(--social-red)"></i>
    <i style="background:var(--social-red)"></i>
    <i style="background:var(--social-red)"></i>
  </div>
  <form class="contact-form">
    <div class="field">Your Name</div>
    <div class="field">Your E-mail</div>
    <div class="field message">Your Message</div>
    <span class="btn">Send Message</span>
  </form>
</section>

<footer class="footer">
  <nav><span>Home</span><span>Services</span><span>About</span><span>Contact</span></nav>
  <span>Copyright © 2024 Step Podiatry. All rights reserved.</span>
</footer>

</body>
</html>
```